Lichtweg Coaching bietet Folgendes an:
- Das KZM (kombinierte, zielbewusste Methodenlehre) Coaching ist eine Kombination aus systematischen, lösungs- und ressourcen-orientierten Methoden. KZM unterstützt Sie, Lösungen zu finden, wo Sie alleine nicht weiterkommen.
-Sonarwirken ist sehr wirkungsvolle energetische Heilmethode, die uns durch die Kraft des Unterbewusstseins ermöglicht, uns von verschiedensten seelischen und körperlichen Beschwerden zu befreien.
https://www.lichtweg-praxis.ch/
Ich wünsche mir für den Newsletter dass das Design steht und ich nur den Text anpassen muss. Evtl bei Clever Reach?
Die Textfarben sind Gold und Himbeerrot (siehe Homepage) https://www.lichtweg-praxis.ch/
schlicht und übersichtlich mit evtl einem Bild. Der Newsletter sollte kreative, ansprechend, neugierig machend und sympathisch sein.
Der Newsletter muss sich mit der Homepage verlinken lassen und der Kunde kann sich an- und abmelden.
Das Impressum und die AGB's der Schweiz sollten enthalten sein.
Alle Infos sind auf meiner Homepage.

```html
<!DOCTYPE html>
<html lang="de">
<head>
<meta charset="utf-8">
<title>Lichtweg Coaching – Newsletter</title>
<link rel="stylesheet" href="https://fonts.googleapis.com/css2?family=Gelasio:ital,wght@0,400;0,700;1,400&family=Arimo:wght@400&display=swap">
<style>
  :root {
    --gold: #b39240;
    --raspberry: #c96a68;
    --page: #eeeeee;
    --paper: #ffffff;
    --band: #d0d0d0;
    --text-grey: #666666;
    --ink: #111111;
    --footer-grey: #8a8a8a;
  }
  * { margin: 0; padding: 0; box-sizing: border-box; }
  html, body {
    width: 1198px; height: 1200px; overflow: hidden;
    background: var(--page);
  }
  body { font-family: "Gelasio", Georgia, serif; }
  .newsletter {
    position: absolute; left: 273px; top: 0;
    width: 653px; height: 1176px;
    background: var(--paper);
    border-top: 3px solid var(--gold);
    border-bottom: 3px solid var(--gold);
  }
  .preheader {
    position: absolute; top: 34px; width: 100%;
    text-align: center; font-size: 15px; color: var(--text-grey);
  }
  .preheader a { color: var(--gold); text-decoration: none; }
  .hero {
    position: absolute; top: 68px; left: 0; width: 653px; height: 154px;
    background: linear-gradient(100deg, #5a5a5a 0%, #9a9a9a 22%, #6e6e6e 45%, #bdbdbd 68%, #7a7a7a 88%, #555 100%);
  }
  .hero-wordmark {
    position: absolute; left: 0; right: 0; top: 46px;
    text-align: center; padding-left: 50px;
    font-weight: 700; font-size: 62px; line-height: 1;
    color: var(--raspberry);
  }
  .brand-title {
    position: absolute; top: 249px; width: 100%;
    text-align: center; font-size: 31px; color: var(--gold); line-height: 1.2;
  }
  .brand-tagline {
    position: absolute; top: 291px; width: 100%;
    text-align: center; font-size: 17px; color: var(--gold);
  }
  .divider {
    position: absolute; top: 350px; left: 16px; right: 16px;
    border-top: 2px solid var(--gold);
  }
  .greeting {
    position: absolute; top: 393px; width: 100%;
    text-align: center; font-size: 21px; color: var(--text-grey);
  }
  .intro {
    position: absolute; top: 438px; left: 18px; right: 18px;
    text-align: center; font-size: 15.5px; line-height: 19.7px; color: var(--text-grey);
  }
  .teaser-band {
    position: absolute; top: 564px; left: 0; width: 100%; height: 363px;
    background: var(--band);
  }
  .teaser-card {
    position: absolute; top: 33px; width: 288px; height: 290px;
    background: var(--paper); padding: 17px 11px 0 11px;
  }
  .teaser-card.blog { left: 27px; }
  .teaser-card.signup { left: 337px; }
  .teaser-card h2 {
    font-weight: 400; font-size: 21.5px; color: var(--ink); line-height: 1.2;
  }
  .teaser-card p {
    margin-top: 16px;
    font-family: "Arimo", Arial, sans-serif;
    font-size: 14.8px; line-height: 19.6px; color: var(--ink);
  }
  .teaser-card a {
    display: inline-block; margin-top: 19px;
    font-family: "Arimo", Arial, sans-serif; font-size: 14.8px;
    color: var(--gold); text-decoration: none;
  }
  .cta-button {
    position: absolute; top: 955px; left: 227px; width: 200px; height: 45px;
    background: var(--gold); border-radius: 6px;
    color: #fff; font-weight: 700; font-size: 16px;
    text-align: center; line-height: 45px; text-decoration: none;
  }
  .imprint {
    position: absolute; top: 1046px; width: 100%;
    text-align: center; font-size: 11px; line-height: 17.5px;
    color: #9a9a9a; filter: blur(1.6px);
  }
  .unsubscribe {
    position: absolute; top: 1133px; width: 100%;
    text-align: center; font-style: italic; font-size: 13px; color: var(--footer-grey);
  }
</style>
</head>
<body>
  <main class="newsletter">
    <p class="preheader">Besuchen Sie hier die <a href="https://www.lichtweg-praxis.ch/">Webversion</a>.</p>

    <div class="hero" role="img" aria-label="Schwarzweissfoto: zwei Hände berühren sich in einer Coaching-Situation">
      <div class="hero-wordmark">Lichtweg</div>
    </div>

    <h1 class="brand-title">LICHTWEG COACHING</h1>
    <p class="brand-tagline">DEINE ZIELE ERREICHEN. DEINEN WEG GEHEN. GESUND SEIN.</p>
    <div class="divider"></div>

    <p class="greeting">Liebe Monika,</p>
    <p class="intro">Molectatatem dem. Luptat utemporias res mod et placcum non eumenie nducienderum faccus eos nihitiandia nos essit, que et offictus dem diciatiatur, autenda volo dollabori cullessum iuressin ea vent, consect ibuscia corepti officaerio et ad utes re nihil isquia dolore sumet moluptatest aut eum que voluptin num id enia deniTium int dolessum</p>

    <section class="teaser-band">
      <article class="teaser-card blog">
        <h2>Hier geht es zum Blog</h2>
        <p>Que et offictus dem diciatiatur, autenda volo dollabori cullessum iuressin ea vent, consect ibuscia corepti officaerio et ad utes re nihil isquia dolore sumet moluptatest aut eum que voluptin num id enia deniTium int dolessum</p>
        <a href="https://www.lichtweg-praxis.ch/">Mehr lesen</a>
      </article>
      <article class="teaser-card signup">
        <h2>Anmeldeformular</h2>
        <p>que et offictus dem diciatiatur, autenda volo dollabori cullessum iuressin ea vent, consect ibuscia corepti officaerio et ad utes re nihil isquia dolore sumet moluptatest aut eum que voluptin num id enia deniTium int dolessum</p>
        <a href="https://www.lichtweg-praxis.ch/">Mehr lesen</a>
      </article>
    </section>

    <a class="cta-button" href="https://www.lichtweg-praxis.ch/">LICHTWEG COACHING</a>

    <footer>
      <p class="imprint">Impressum<br>Lichtweg Coaching<br>Sonnenrain 4<br>8000 Zürich</p>
      <p class="unsubscribe">Newsletter abbestellen</p>
    </footer>
  </main>
</body>
</html>
```